Harbor Leaf Salvage Centre

Text draft only
‘HELP! Stop toxic landfill pollution’
Australians are addicted to all forms new electronic equipment, we consume more per head of population than any country on the Planet!On average we now ditch a television each 2 years, we purchase the latest smart phone every year, the latest computer each year, SME’s and large corporation companies change IT hardware each 12 months. We purchased 17 million items new electronic purchases in 2011! The kicker is: (only 2.4 million) were correctly recycled.
If you are rolling over your IT Hardware, phones, or printers think first harbor Leaf Salvage, for a small fee we will correctly recycle your old E-Waste.
World standard ISO 14001.

‘TOGETHER WE CAN MAKE A DIFFERENCE’
THE NEW HARBOR LEAF SALVAGE CENTRE
47 Marlow St Kendrick
Opening hours: 8am – 4.pm Week days and 9am – midday Saturdays.
www.harborleafsalvage.example
1300 58 26 91

```html
<!DOCTYPE html>
<html lang="en">
<head>
<meta charset="utf-8">
<title>Harbor Leaf Salvage Centre – Stop Toxic Landfill Pollution</title>
<link rel="stylesheet" href="https://fonts.googleapis.com/css2?family=Gochi+Hand&family=Courier+Prime:wght@700&family=Arimo:wght@400;700&display=swap">
<style>
  :root {
    --sky-top: #1f7fe0;
    --sky-mid: #3d9cf0;
    --sky-low: #7cc0f5;
    --cloud: rgba(255,255,255,0.55);
    --grass-light: #8fd23c;
    --grass-mid: #4f9a1c;
    --grass-dark: #2c6410;
    --headline: #ffffff;
    --body-ink: #0b1733;
    --sand: #d9c18f;
    --sand-dark: #b99a5e;
    --footer-ink: #141414;
    --brand-green: #3c8a2a;
  }
  * { box-sizing: border-box; margin: 0; padding: 0; }
  html, body { width: 845px; height: 1200px; overflow: hidden; }
  body { background: var(--sky-mid); }
  .poster {
    position: relative;
    width: 845px;
    height: 1200px;
    overflow: hidden;
    background:
      radial-gradient(ellipse 260px 90px at 760px 560px, var(--cloud), transparent 70%),
      radial-gradient(ellipse 220px 70px at 720px 30px, var(--cloud), transparent 70%),
      radial-gradient(ellipse 200px 80px at 120px 1020px, rgba(255,255,255,0.4), transparent 70%),
      radial-gradient(ellipse 260px 90px at 780px 980px, rgba(255,255,255,0.4), transparent 70%),
      linear-gradient(180deg, var(--sky-top) 0%, var(--sky-mid) 45%, var(--sky-low) 100%);
  }
  .hero-globe {
    position: absolute;
    left: 60px;
    top: 20px;
    width: 700px;
    height: 720px;
  }
  .headline {
    position: absolute;
    left: 0;
    width: 845px;
    top: 738px;
    text-align: center;
    font-family: "Gochi Hand", cursive;
    font-size: 50px;
    font-style: italic;
    color: var(--headline);
    letter-spacing: 1px;
    line-height: 1;
    text-shadow: 0 1px 2px rgba(0,0,0,0.25);
  }
  .body-copy {
    position: absolute;
    left: 57px;
    top: 798px;
    width: 732px;
    font-family: "Courier Prime", "Courier New", monospace;
    font-weight: 700;
    font-size: 16.5px;
    letter-spacing: 0.8px;
    line-height: 26.2px;
    color: var(--body-ink);
    text-align: justify;
  }
  .footer-band {
    position: absolute;
    left: 0;
    top: 1058px;
    width: 845px;
    height: 142px;
  }
  .brand {
    position: absolute;
    left: 30px;
    top: 1112px;
    display: flex;
    align-items: center;
    gap: 12px;
  }
  .brand-dot {
    width: 66px;
    height: 66px;
    border-radius: 50%;
    background: var(--brand-green);
  }
  .brand-name {
    font-family: "Arimo", Arial, sans-serif;
    font-weight: 700;
    font-size: 28px;
    color: var(--footer-ink);
    letter-spacing: -0.5px;
  }
  .contact {
    position: absolute;
    right: 29px;
    top: 1087px;
    text-align: right;
    font-family: "Arimo", Arial, sans-serif;
    color: var(--footer-ink);
    font-size: 11.5px;
    line-height: 18.4px;
    letter-spacing: 0.6px;
  }
  .contact .tagline,
  .contact .centre-name {
    font-weight: 700;
    font-size: 12.5px;
    letter-spacing: 1px;
  }
</style>
</head>
<body>
<main class="poster">
  <svg class="hero-globe" viewBox="0 0 700 720" role="img" aria-label="Illustration of a small grassy planet with trees, flowers, a butterfly and a dove on top, and discarded computers, keyboards, printers, circuit boards and mobile phones piled around its lower half">
    <defs>
      <radialGradient id="globe-grass" cx="45%" cy="38%" r="60%">
        <stop offset="0%" stop-color="var(--grass-light)"/>
        <stop offset="60%" stop-color="var(--grass-mid)"/>
        <stop offset="100%" stop-color="var(--grass-dark)"/>
      </radialGradient>
      <radialGradient id="globe-glow" cx="50%" cy="50%" r="50%">
        <stop offset="80%" stop-color="#ffffff" stop-opacity="0.45"/>
        <stop offset="100%" stop-color="#ffffff" stop-opacity="0"/>
      </radialGradient>
    </defs>
    <circle cx="352" cy="376" r="320" fill="url(#globe-glow)"/>
    <circle cx="352" cy="376" r="270" fill="url(#globe-grass)"/>
  </svg>

  <h1 class="headline">HELP! STOP TOXIC LANDFILL POLLUTION!</h1>

  <p class="body-copy">Australians are addicted to all forms new electronic equipment, we consume more per head of population than any country on the Planet! On average we now ditch a television each 2 years, we purchase the latest smart phone every year, the latest computer each year, SME’s and large corporation companies change IT hardware each 12 months. We purchased 17 million items new electronic purchases in 2011! The kicker is: (only 2.4 million) were correctly recycled. If you are rolling over your IT Hardware, phones, or printers think first harbor Leaf Salvage, for a small fee we will correctly recycle your old E-Waste. World standard ISO 14001.</p>

  <svg class="footer-band" viewBox="0 0 845 142" preserveAspectRatio="none" aria-hidden="true">
    <defs>
      <linearGradient id="sand-fill" x1="0" y1="0" x2="0" y2="1">
        <stop offset="0%" stop-color="var(--sand)"/>
        <stop offset="100%" stop-color="var(--sand-dark)"/>
      </linearGradient>
    </defs>
    <path d="M0 14 L40 10 L85 16 L130 8 L180 14 L230 9 L275 15 L320 6 L370 12 L420 8 L470 15 L520 7 L570 13 L620 9 L665 16 L710 6 L760 12 L805 5 L845 10 L845 142 L0 142 Z" fill="url(#sand-fill)"/>
  </svg>

  <div class="brand">
    <span class="brand-dot"></span>
    <span class="brand-name">Harbor Leaf Salvage</span>
  </div>

  <address class="contact">
    <div class="tagline">TOGETHER WE CAN MAKE A DIFFERENCE</div>
    <div class="centre-name">THE NEW HARBOR LEAF SALVAGE CENTRE</div>
    <div>47 Marlow St Kendrick</div>
    <div>Opening hours: 8am–4pm Week days;9am–midday Saturdays.</div>
    <div>www.harborleafsalvage.example 1300 58 26 91</div>
  </address>
</main>
</body>
</html>
```